Cleaning service website design

We need a new nice web design(logo will be the same) for a new cleaning service Company:

Informations about Company and logo you can take from flyers in attachments.

This is a cleaning service Company which have simple rules and we would like to show that(in checklist form) on website:

- What we do and that we're Cleaning Green

- Why us?

- How much(our pricing is simple)

Also we would like to communicate with clients by some nice/big pictures on website and the most important thing is our phone number and short/fast Freestimate.

Also there should be some space for description about our Company.

Generally all information on main page can be short: about us, about service(what we do), last reviews, tips (for example: Tip of the week) and other can be some introduction to subpage where will be more information.

There will be few subpages like: About us, About our service, Photos(Before and after), Reviews , Tips, FAQ, Contact, Looking for a Job? - most of them will be just text so you can project just one example.

```html
<!DOCTYPE html>
<html lang="en">
<head>
<meta charset="utf-8">
<title>Tidy Nest — House Cleaning</title>
<link href="https://fonts.googleapis.com/css2?family=Lato:ital,wght@0,400;0,700;1,400&family=Josefin+Sans:wght@300;400;700&family=Yellowtail&family=Fredoka:wght@600&display=swap" rel="stylesheet">
<style>
:root{
  --green:#6bbd58;
  --green-dark:#4e9d3d;
  --blue:#0a58a8;
  --blue-dark:#0b4a8f;
  --yellow:#fbb817;
  --ink:#333;
  --muted:#7d7d7d;
  --line:#e2e2e2;
  --page:#fff;
}
*{margin:0;padding:0;box-sizing:border-box}
html,body{width:777px;height:1200px;overflow:hidden;background:var(--page)}
body{position:relative;font-family:"Lato",sans-serif;color:var(--ink)}
.abs{position:absolute}

/* nav */
.main-nav{left:0;top:0;width:777px;height:26px;border-bottom:1px solid var(--line);display:flex;justify-content:center}
.main-nav a{font-size:7.5px;letter-spacing:.4px;color:#444;text-decoration:none;padding:0 14px;line-height:26px;text-transform:uppercase}
.main-nav a.active{border-bottom:2px solid var(--green)}

/* header */
.call{left:117px;top:48px;display:flex;align-items:center;gap:6px;white-space:nowrap}
.call-label{font-family:"Yellowtail",cursive;color:var(--blue);font-size:12px}
.call-number{font-weight:700;font-size:14px;color:#333;letter-spacing:.3px}
.brand{left:338px;top:42px;width:114px;height:66px;border-radius:50%;background:#fff;border:4px solid var(--blue);display:flex;align-items:center;justify-content:center;gap:5px;z-index:3}
.brand-dot{width:12px;height:12px;border-radius:50%;background:var(--green)}
.brand-name{font-family:"Lato",sans-serif;font-weight:700;font-size:14px;color:var(--green-dark);white-space:nowrap}
.follow{left:545px;top:47px;display:flex;align-items:center;gap:4px;white-space:nowrap}
.follow-label{font-family:"Yellowtail",cursive;color:var(--blue);font-size:12px;margin-right:4px}
.social{width:13px;height:13px;border-radius:50%}

/* hero */
.hero{left:0;top:82px;width:777px;height:265px;background:linear-gradient(90deg,#8a6a47 0%,#b79a72 35%,#d9c2a0 60%,#c9a57a 100%)}
.hero-photo{left:380px;top:78px;width:340px;height:269px;background:linear-gradient(180deg,#e7d6c6 0%,#2d5fb0 55%,#244f97 100%);border-radius:120px 120px 0 0;opacity:.9}
.hero-title{left:120px;top:134px;width:250px;font-family:"Josefin Sans",sans-serif;font-weight:700;font-size:27px;line-height:32px;color:#fff;letter-spacing:.5px;white-space:nowrap;text-shadow:0 1px 3px rgba(0,0,0,.4)}
.hero-rule{left:118px;top:219px;width:243px;height:2px;background:#fff}
.hero-tag{left:197px;top:210px;background:#fff;padding:2px 10px;font-family:"Yellowtail",cursive;color:var(--blue);font-size:11px;white-space:nowrap}
.hero-sub{left:118px;top:238px;width:243px;text-align:center;font-weight:700;font-size:10.5px;line-height:13px;color:#fff;text-transform:uppercase}
.hero-rule2{left:118px;top:270px;width:243px;height:2px;background:#fff}
.arrow-btn{width:40px;height:40px;border-radius:50%;border:1.5px solid #fff;display:flex;align-items:center;justify-content:center}

/* pills */
.pills{display:grid;grid-template-columns:136px 104px;gap:2px 4px}
.pill{height:14px;border-radius:8px;background:var(--blue);color:#fff;font-size:7.5px;display:flex;align-items:center;gap:5px;padding-left:8px;white-space:nowrap}
.pill svg,.svc svg{flex:none}

/* pricing */
.section-title{left:0;width:777px;text-align:center;font-family:"Josefin Sans",sans-serif;font-weight:300;font-size:27px;letter-spacing:1px;color:#444;white-space:nowrap}
.price{top:420px;width:173px;height:98px;overflow:hidden}
.price-photo{right:0;top:0;width:82px;height:98px}
.price-amount{left:14px;top:6px;font-family:"Yellowtail",cursive;color:#fff;font-size:36px;line-height:40px}
.price-bar{left:15px;top:48px;width:63px;height:2px;background:#fff}
.price-text{left:15px;top:52px;color:#fff;font-size:10px;line-height:12px;text-transform:uppercase}

/* about */
.divider{left:0;top:547px;width:777px;height:1px;background:var(--line)}
.script-head{font-family:"Yellowtail",cursive;color:var(--green);font-size:18px;white-space:nowrap}
.caps-head{font-size:10.5px;letter-spacing:.5px;color:#333;text-transform:uppercase;white-space:nowrap}
.body-copy{font-size:8.5px;line-height:10.6px;color:var(--muted);text-align:justify}
.col-rule{left:388px;top:580px;width:1px;height:185px;background:var(--line)}

/* services */
.services-title{left:0;top:786px;width:777px;text-align:center;font-family:"Josefin Sans",sans-serif;font-weight:300;font-size:32px;color:var(--green)}
.services-band{left:0;top:816px;width:777px;height:113px;background:var(--green)}
.svc-col{top:833px;display:flex;flex-direction:column}
.svc{height:16px;color:#fff;font-size:8px;display:flex;align-items:center;gap:6px;padding-left:8px;border-radius:8px;white-space:nowrap}
.svc.highlight{background:var(--green-dark);width:173px}

/* tip + reviews */
.tip-box{left:117px;top:969px;width:304px;height:109px;background:#f4f4f4;border:1px solid #e6e6e6}
.tip-photo{left:117px;top:969px;width:105px;height:109px}
.tip-title{left:226px;top:980px;font-family:"Fredoka",sans-serif;font-size:18px;color:var(--green);letter-spacing:1px;text-transform:uppercase;white-space:nowrap}
.tip-sub{left:226px;top:1006px;font-size:7.5px;color:#333;text-transform:uppercase;white-space:nowrap}
.tip-copy{left:226px;top:1017px;width:184px;font-size:7px;line-height:9px;color:var(--muted);text-align:justify}
.review-head{left:440px;top:970px}
.avatar{left:440px;top:997px;width:58px;height:64px}
.reviewer{left:505px;top:996px;font-size:7.5px;color:#333;white-space:nowrap}
.reviewer small{font-size:5.5px;color:#555}
.review-copy{left:505px;top:1006px;width:154px;font-size:6.5px;line-height:8.4px;color:#777;font-style:italic}
.read-more{left:505px;top:1052px;font-size:6.5px;color:#d23;font-style:italic}
.dots{left:442px;top:1072px;display:flex;gap:2px}
.dots span{width:6px;height:6px;border-radius:50%;background:#ddd}
.dots span.on{background:var(--blue)}

/* footer */
.footer{left:0;top:1132px;width:777px;height:68px;background:var(--blue)}
.footer-brand{left:354px;top:1110px;width:70px;height:42px;border-radius:50%;background:#fff;border:3px solid var(--blue);display:flex;align-items:center;justify-content:center;gap:3px}
.footer-brand .brand-name{font-size:9px}
.footer-brand .brand-dot{width:7px;height:7px}
.footer-links{left:0;top:1160px;width:777px;text-align:center;font-size:7.5px;color:#fff;white-space:nowrap}
.footer-links a{color:#fff;text-decoration:none;padding:0 4px}
.copyright{left:0;top:1173px;width:777px;text-align:center;font-size:7px;color:#fff}
</style>
</head>
<body>

<nav class="main-nav abs">
  <a href="#">About Us</a><a href="#" class="active">About Our Service</a><a href="#">Photos</a><a href="#">Reviews</a><a href="#">Tips</a><a href="#">FAQ</a><a href="#">Contact</a><a href="#">Looking for a Job?</a>
</nav>

<div class="call abs">
  <svg width="16" height="16" viewBox="0 0 16 16"><circle cx="8" cy="8" r="8" fill="var(--blue)"/><path d="M5 4.5l1.6-.4 1 2-1 .8a5 5 0 0 0 2.5 2.5l.8-1 2 1-.4 1.6c-3.6.2-6.7-2.9-6.5-6.5z" fill="#fff"/></svg>
  <span class="call-label">Call us Today</span>
  <span class="call-number">289-555-0148</span>
</div>

<div class="brand abs"><span class="brand-dot"></span><span class="brand-name">Tidy Nest</span></div>

<div class="follow abs">
  <span class="follow-label">Follow Us</span>
  <span class="social" style="background:#3b5a9a"></span>
  <span class="social" style="background:#2aa3d8"></span>
  <span class="social" style="background:#1f6fa8"></span>
  <span class="social" style="background:#d2312a"></span>
</div>

<section class="hero abs" role="img" aria-label="Bright living room interior, softly blurred"></section>
<div class="hero-photo abs" role="img" aria-label="Smiling housekeeper in a blue apron holding a mop and spray bottle"></div>
<h1 class="hero-title abs">WHAT DO WE<br>CLEANON EVERY</h1>
<div class="hero-rule abs"></div>
<div class="hero-tag abs">Our Services</div>
<p class="hero-sub abs">Thoroughly clean your bathrooms, kitchen, bedrooms and living areas</p>
<div class="hero-rule2 abs"></div>
<div class="pills abs" style="left:117px;top:284px">
  <span class="pill"><svg width="9" height="6" viewBox="0 0 9 6"><path d="M1 3l2 2 5-4" stroke="#fff" fill="none" stroke-width="1.3"/></svg>Mop or vacuum your floors</span>
  <span class="pill"><svg width="9" height="6" viewBox="0 0 9 6"><path d="M1 3l2 2 5-4" stroke="#fff" fill="none" stroke-width="1.3"/></svg>Collect garbage</span>
  <span class="pill"><svg width="9" height="6" viewBox="0 0 9 6"><path d="M1 3l2 2 5-4" stroke="#fff" fill="none" stroke-width="1.3"/></svg>Dust surfaces</span>
  <span class="pill"><svg width="9" height="6" viewBox="0 0 9 6"><path d="M1 3l2 2 5-4" stroke="#fff" fill="none" stroke-width="1.3"/></svg>Make beds</span>
</div>
<a class="arrow-btn abs" style="left:51px;top:193px" href="#" aria-label="Previous"><svg width="10" height="12" viewBox="0 0 10 12"><path d="M7 1L2 6l5 5" stroke="#fff" stroke-width="2" fill="none"/></svg></a>
<a class="arrow-btn abs" style="left:681px;top:193px" href="#" aria-label="Next"><svg width="10" height="12" viewBox="0 0 10 12"><path d="M3 1l5 5-5 5" stroke="#fff" stroke-width="2" fill="none"/></svg></a>

<h2 class="section-title abs" style="top:374px">OUR MAID SERVICE PRICING IS SIMPLE TOO</h2>

<div class="price abs" style="left:117px;background:var(--green)">
  <div class="price-photo abs" role="img" aria-label="Cleaner seen from behind with gloves on hips" style="background:linear-gradient(180deg,#e9d6b8,#3457a6 60%,#e9e3dc)"></div>
  <div class="price-amount abs">$79</div><div class="price-bar abs"></div>
  <div class="price-text abs">For homes<br>less than<br>1000 sq. ft.</div>
</div>
<div class="price abs" style="left:302px;background:var(--yellow)">
  <div class="price-photo abs" role="img" aria-label="Cleaner in green apron giving thumbs up" style="background:linear-gradient(180deg,#fbc24a,#2d7a3a 75%)"></div>
  <div class="price-amount abs">$89</div><div class="price-bar abs"></div>
  <div class="price-text abs">For homes<br>1000-1800<br>sq. ft.</div>
</div>
<div class="price abs" style="left:487px;background:var(--blue)">
  <div class="price-photo abs" role="img" aria-label="Cleaner holding a blue cloth and spray bottle" style="background:linear-gradient(180deg,#2a6fc0,#f3eee8 70%)"></div>
  <div class="price-amount abs">$99</div><div class="price-bar abs"></div>
  <div class="price-text abs">For homes<br>2,300-3,000<br>square feet*</div>
</div>

<div class="divider abs"></div>

<div class="abs" style="left:117px;top:586px;width:253px">
  <div class="script-head">Why Choose Us?</div>
  <div class="caps-head">It's about caring, not just cleaning.</div>
  <p class="body-copy" style="margin-top:14px">Have you ever wondered what it would be like if your life was simpler? We're here to help by taking over the chore of house cleaning. You'll have more time to spend on the things that matter most to you. With Tidy Nest you get reliable, trustworthy and affordable maid service. We pay attention to your needs. We get the job done!</p>
</div>
<div class="pills abs" style="left:117px;top:716px">
  <span class="pill"><svg width="9" height="6" viewBox="0 0 9 6"><path d="M1 3l2 2 5-4" stroke="#fff" fill="none" stroke-width="1.3"/></svg>Mop or vacuum your floors</span>
  <span class="pill"><svg width="9" height="6" viewBox="0 0 9 6"><path d="M1 3l2 2 5-4" stroke="#fff" fill="none" stroke-width="1.3"/></svg>Collect garbage</span>
  <span class="pill"><svg width="9" height="6" viewBox="0 0 9 6"><path d="M1 3l2 2 5-4" stroke="#fff" fill="none" stroke-width="1.3"/></svg>Dust surfaces</span>
  <span class="pill"><svg width="9" height="6" viewBox="0 0 9 6"><path d="M1 3l2 2 5-4" stroke="#fff" fill="none" stroke-width="1.3"/></svg>Make beds</span>
</div>
<div class="col-rule abs"></div>
<div class="abs" style="left:405px;top:586px;width:253px">
  <div class="script-head">Halton Region House Cleaning Services</div>
  <div class="caps-head">House cleaning...made easy!</div>
  <p class="body-copy" style="margin-top:14px">We are Marek and Anna Kowal and we have personally experienced the struggle of finding a reliable and affordable maid service. We understand how busy life can be and cleaning is one of the tasks that falls off the list when you're stretched too thin. We are here to help! Let Tidy Nest take care of the house cleaning so you can focus on the more important things in life.</p>
  <p class="body-copy" style="margin-top:10px">Halton, Burlington, Oakville and Milton residents can count on us to make your home sparkle from top to bottom!</p>
</div>

<div class="services-band abs"></div>
<h2 class="services-title abs">Our Services</h2>
<div class="svc-col abs" style="left:117px">
  <span class="svc"><svg width="9" height="6" viewBox="0 0 9 6"><path d="M1 3l2 2 5-4" stroke="#fff" fill="none" stroke-width="1.3"/></svg>Thoroughly clean your bathrooms</span>
  <span class="svc highlight"><svg width="9" height="6" viewBox="0 0 9 6"><path d="M1 3l2 2 5-4" stroke="#fff" fill="none" stroke-width="1.3"/></svg>Carefully clean the kitchen</span>
  <span class="svc"><svg width="9" height="6" viewBox="0 0 9 6"><path d="M1 3l2 2 5-4" stroke="#fff" fill="none" stroke-width="1.3"/></svg>Tidy up around the house</span>
  <span class="svc"><svg width="9" height="6" viewBox="0 0 9 6"><path d="M1 3l2 2 5-4" stroke="#fff" fill="none" stroke-width="1.3"/></svg>Dusting of surfaces</span>
  <span class="svc"><svg width="9" height="6" viewBox="0 0 9 6"><path d="M1 3l2 2 5-4" stroke="#fff" fill="none" stroke-width="1.3"/></svg>Making mirrors shine</span>
</div>
<div class="svc-col abs" style="left:317px">
  <span class="svc"><svg width="9" height="6" viewBox="0 0 9 6"><path d="M1 3l2 2 5-4" stroke="#fff" fill="none" stroke-width="1.3"/></svg>Make beds</span>
  <span class="svc"><svg width="9" height="6" viewBox="0 0 9 6"><path d="M1 3l2 2 5-4" stroke="#fff" fill="none" stroke-width="1.3"/></svg>Vacuuming rugs and carpeted areas</span>
  <span class="svc"><svg width="9" height="6" viewBox="0 0 9 6"><path d="M1 3l2 2 5-4" stroke="#fff" fill="none" stroke-width="1.3"/></svg>Cleaning of hardwood/tile/linoleum floors</span>
  <span class="svc"><svg width="9" height="6" viewBox="0 0 9 6"><path d="M1 3l2 2 5-4" stroke="#fff" fill="none" stroke-width="1.3"/></svg>Emptying garbage</span>
  <span class="svc"><svg width="9" height="6" viewBox="0 0 9 6"><path d="M1 3l2 2 5-4" stroke="#fff" fill="none" stroke-width="1.3"/></svg>including toilet</span>
</div>
<div class="svc-col abs" style="left:527px">
  <span class="svc"><svg width="9" height="6" viewBox="0 0 9 6"><path d="M1 3l2 2 5-4" stroke="#fff" fill="none" stroke-width="1.3"/></svg>Sink</span>
  <span class="svc"><svg width="9" height="6" viewBox="0 0 9 6"><path d="M1 3l2 2 5-4" stroke="#fff" fill="none" stroke-width="1.3"/></svg>Shower and tub</span>
  <span class="svc"><svg width="9" height="6" viewBox="0 0 9 6"><path d="M1 3l2 2 5-4" stroke="#fff" fill="none" stroke-width="1.3"/></svg>Countertops</span>
  <span class="svc"><svg width="9" height="6" viewBox="0 0 9 6"><path d="M1 3l2 2 5-4" stroke="#fff" fill="none" stroke-width="1.3"/></svg>Outside of Appliances</span>
  <span class="svc"><svg width="9" height="6" viewBox="0 0 9 6"><path d="M1 3l2 2 5-4" stroke="#fff" fill="none" stroke-width="1.3"/></svg>Tidy up around the house</span>
</div>

<div class="tip-box abs"></div>
<div class="tip-photo abs" role="img" aria-label="Cheerful cleaner in red apron with yellow gloves giving thumbs up" style="background:linear-gradient(180deg,#f1e9e2 0%,#f2d14a 55%,#d8343a 100%)"></div>
<div class="tip-title abs">Tip of the Week</div>
<div class="tip-sub abs">It's about caring, not just cleaning.</div>
<p class="tip-copy abs">Have you ever wondered what it would be like if your life was simpler? We're here to help by taking over the chore of house cleaning. You'll have more time to spend on the things that matter most to you.</p>

<div class="review-head script-head abs">Latest Reviews</div>
<div class="avatar abs" role="img" aria-label="Portrait photo of the reviewer" style="background:linear-gradient(160deg,#4a3a30,#b08a70 60%,#5b7a3a)"></div>
<div class="reviewer abs">DANA R. <small>MEMPHIS, TN</small>
  <svg width="38" height="7" viewBox="0 0 38 7" style="margin-left:3px;vertical-align:-1px"><g fill="var(--yellow)"><circle cx="3.5" cy="3.5" r="3"/><circle cx="11" cy="3.5" r="3"/><circle cx="18.5" cy="3.5" r="3"/></g><circle cx="26" cy="3.5" r="3" fill="#222"/></svg>
</div>
<p class="review-copy abs">"Came by and gave me an estimate around 10am and they were here at 4:30pm that same Friday. I needed a one time end of summer clean. Prices were not bad for a crew of four and they easily collaborated and focused on the areas..</p>
<div class="read-more abs">Read more...</div>
<div class="dots abs"><span></span><span class="on"></span><span></span></div>

<footer class="footer abs"></footer>
<div class="footer-brand abs"><span class="brand-dot"></span><span class="brand-name">Tidy Nest</span></div>
<div class="footer-links abs">
  <a href="#">About Us</a>|<a href="#">About Our Service</a>|<a href="#">Photos</a>|<a href="#">Reviews</a>|<a href="#">Tips</a>|<a href="#">FAQ</a>|<a href="#">Contact</a>|<a href="#">Looking for a Job?</a>
</div>
<div class="copyright abs">Copyright © 2013 Tidy Nest</div>

</body>
</html>
```